Business Card & Logo Design - Hedge Fund

We need a business card and logo design for a hedge fund. The hedge fund is named Morvane Holdings LLC. Morvane Holdings was created by finance professors and the strategy is based academic research that looks for patterns in stock prices. The design should look conservative, solid, strong. We favor a classic style - nothing flashy. The logo can relate to the name Morvane Holdings, or it could involve a symbol design that connotes "science" . We are open to ideas. We do not want alot of colors - but if any, color - blue is preferred. The font that seems to look best for the name (Morvane Holdings) is arial black. We are open to ideas. Most important - we want to see a mock up of an actual business card with the logo concept embedded. The business card should include space for : company name, individual name, position title, cell phone, address. We hope to have this work done by Sept. 8.

Target Market(s)

We will be meeting with and giving the business card to institutions and high net worth individuals.

Industry/Entity Type

Investment Advisory

Contact Information for Business Card

Company name - Morvane Holdings LLC
Individual name - Peter Vosk
Title - Portfolio Manager
Cell - (482) 555-0137
Address - 2750 Birchwell Lane, Suite 300, Atlanta GA 30327

Font styles to use
Other font styles liked:
• Arial

Colors
3277b5
0255a3
85acd3
cedeed
fdf9cf
d9d9d9
e6e6e6
f04a50
6b449b

Requirements
Must have
• Must have card details that are sited above.
• We would like a logo related to the name (Morvane Holdings) or concept of the fund.
Nice to have
• We want conservative / understated / clean crisp look.
• If any colors - we prefer conservative appearance - blue / gray.
• I have enclosed an example of a card style that looks attractive - please do not exactly copy this card. This is not our company or logo. I feel the layout is attractive - just as an example
Should not have
• Avoid too much color.
• I have selected some preferred colors. Please do not use all of the colors - I have selected a few that might work - but I am not sure. We are open to your ideas so please do not feel the need to use all or any of these.

```html
<!DOCTYPE html>
<html lang="en">
<head>
<meta charset="utf-8">
<title>Morvane Holdings — Business Card</title>
<link rel="stylesheet" href="https://fonts.googleapis.com/css2?family=Montserrat:wght@400;500;800&display=swap">
<style>
  :root {
    --navy: #363762;
    --ink: #2f2f38;
    --rule: #b9b9bf;
    --paper: #f9f9f9;
    --backdrop: #ececec;
    --shadow: rgba(0, 0, 0, 0.12);
  }
  * { box-sizing: border-box; margin: 0; padding: 0; }
  html, body {
    width: 1200px;
    height: 1189px;
    overflow: hidden;
    background: var(--backdrop);
    font-family: "Montserrat", Arial, sans-serif;
  }
  .stage { position: relative; width: 1200px; height: 1189px; }

  .card {
    position: absolute;
    width: 700px;
    height: 400px;
    box-shadow: 0 10px 30px var(--shadow);
  }
  .card--back {
    left: 420px;
    top: 150px;
    background: var(--navy);
    display: flex;
    flex-direction: column;
    align-items: center;
    justify-content: center;
    gap: 34px;
  }
  .card--front {
    left: 80px;
    top: 630px;
    background: var(--paper);
    display: flex;
    align-items: center;
  }

  .wordmark {
    display: flex;
    align-items: center;
    gap: 14px;
    font-weight: 800;
    font-size: 34px;
    letter-spacing: 1px;
    text-transform: uppercase;
    line-height: 1;
  }
  .wordmark__square { width: 22px; height: 22px; flex: none; }
  .card--back .wordmark { color: #ffffff; }
  .card--back .wordmark__square { background: #ffffff; }
  .card--front .wordmark { color: var(--navy); font-size: 24px; gap: 10px; }
  .card--front .wordmark__square { background: var(--navy); width: 16px; height: 16px; }

  .back-url {
    color: #ffffff;
    font-size: 17px;
    font-weight: 500;
    letter-spacing: 1px;
  }

  .front-brand {
    width: 350px;
    display: flex;
    justify-content: center;
  }
  .front-divider {
    width: 1px;
    height: 150px;
    background: var(--rule);
  }
  .contact {
    padding-left: 40px;
    color: var(--ink);
    font-size: 15px;
    line-height: 1.45;
  }
  .contact__name {
    color: var(--navy);
    font-size: 26px;
    font-weight: 800;
    line-height: 1.1;
  }
  .contact__title { font-size: 15px; margin-bottom: 14px; }
  .contact__address { margin-bottom: 6px; }
  .contact__row { display: flex; align-items: center; gap: 10px; }
  .contact__icon { width: 14px; height: 14px; flex: none; }
</style>
</head>
<body>
<main class="stage">

  <section class="card card--back" aria-label="Card back">
    <div class="wordmark"><span class="wordmark__square"></span>Morvane Holdings</div>
    <p class="back-url">www.morvaneholdings.com</p>
  </section>

  <section class="card card--front" aria-label="Card front">
    <div class="front-brand">
      <div class="wordmark"><span class="wordmark__square"></span>Morvane Holdings</div>
    </div>
    <div class="front-divider"></div>
    <div class="contact">
      <p class="contact__name">Peter Vosk</p>
      <p class="contact__title">Portfolio Manager</p>
      <p class="contact__address">2750 Birchwell Lane<br>Suite 300, Atlanta GA 30327</p>
      <p class="contact__row">
        <svg class="contact__icon" viewBox="0 0 16 16" aria-hidden="true"><path d="M4 1.5 6 5 4.6 6.6c.9 1.9 2.4 3.4 4.3 4.3L10.5 9.5 14 11.5l-.8 2.6c-6.2.3-11.4-4.9-11.2-11.2z" fill="none" stroke="#363762" stroke-width="1.4" stroke-linejoin="round"/></svg>
        (482) 555-0137
      </p>
      <p class="contact__row">
        <svg class="contact__icon" viewBox="0 0 16 16" aria-hidden="true"><rect x="1.5" y="3.5" width="13" height="9" fill="none" stroke="#363762" stroke-width="1.4"/><path d="M1.5 3.5 8 9l6.5-5.5" fill="none" stroke="#363762" stroke-width="1.4"/></svg>
        peter@morvaneholdings.com
      </p>
      <p class="contact__row">
        <svg class="contact__icon" viewBox="0 0 16 16" aria-hidden="true"><circle cx="8" cy="8" r="6.5" fill="none" stroke="#363762" stroke-width="1.3"/><ellipse cx="8" cy="8" rx="2.8" ry="6.5" fill="none" stroke="#363762" stroke-width="1.1"/><path d="M1.5 8h13" stroke="#363762" stroke-width="1.1"/></svg>
        www.morvaneholdings.com
      </p>
    </div>
  </section>

</main>
</body>
</html>
```